Modern Retail Coffee Label for established Roastery! 17 years!

We are looking for a Retail Coffee Bag Label... JUST THE LABEL TO GO ON AN EXISTING BAG. Our current label is provided and our Logo.. we have had the same Red Bags FOREVER so we are looking for a label to compliment that tradition and to be placed on the bags we have used for 17 years.

We have a retail line of bags with locally roasted coffee. Our business has been around 17years and is in need of a design upgrade! We have a red coffee bag and are looking for a sleek modern label. I will attach a file of our label right now so you can see what it looks like. We are just looking for a more modern version. a few inclusions:

Locally Roasted
100% Arabica Coffee
Heron Sister's Roasters
heronsisroasters.example
logo

The black label with the red and yellow color label is the old one... the new label should be the White background and black border one...

Target Market(s)

Retail Coffee Consumers

Font styles to use
Other font styles liked:
• use what you think. we are located in SW Wisconsin but ship coffee EVERYWHERE

Colors

Designer to choose only greyscale colors for use in the design.

Requirements
Must have
• Locally Roasted (Platteville,WI)
• 100% Arabica Coffee
• heronsisroasters.example
• logo
Nice to have
• Badgers
• "Since 2003"
Should not have
• Any tallmugs or big brand themes

```html
<!DOCTYPE html>
<html lang="en">
<head>
<meta charset="utf-8">
<title>Heron Sister's Roasters – Retail Label</title>
<link rel="stylesheet" href="https://fonts.googleapis.com/css2?family=Bitter:wght@700;800&family=Sancreek&display=swap">
<style>
  :root {
    --frame: #0b0b0b;
    --paper: #f1f1f1;
    --ink: #1f1d1e;
    --slate: #3d3d40;
    --logo-box: #4a4a4c;
    --logo-splash: #6a6a6c;
    --mocha-dark: #5b4a40;
    --mocha-light: #c9c2be;
    --band: #8a7d77;
  }
  * { margin: 0; padding: 0; box-sizing: border-box; }
  html, body { width: 936px; height: 1200px; overflow: hidden; background: #fff; }
  .label {
    position: relative;
    width: 936px; height: 1200px;
    background: var(--frame);
    overflow: hidden;
  }
  .panel {
    position: absolute;
    left: 38px; top: 36px; right: 34px; bottom: 34px;
    background: var(--paper);
    border-radius: 40px;
  }
  .logo-splash {
    position: absolute;
    left: 190px; top: 58px; width: 440px; height: 330px;
    background: radial-gradient(ellipse at 55% 40%, var(--logo-splash) 0%, rgba(106,106,108,0.35) 60%, rgba(106,106,108,0) 78%);
    border-radius: 30px;
  }
  .logo-box {
    position: absolute;
    left: 283px; top: 94px; width: 344px; height: 198px;
    background: var(--logo-box);
    border-radius: 22px;
  }
  .logo-plate {
    position: absolute;
    left: 328px; top: 133px; width: 254px; height: 142px;
    border: 4px solid #fff;
    border-radius: 8px;
    display: flex; flex-direction: column; align-items: center; justify-content: center;
    gap: 8px;
  }
  .logo-name {
    font-family: "Bitter", serif;
    font-weight: 800;
    color: #fff;
    font-size: 28px;
    letter-spacing: 1px;
    text-align: center;
    line-height: 1.15;
  }
  .since {
    position: absolute;
    left: 490px; top: 334px;
    font-family: "Bitter", serif; font-weight: 800;
    font-size: 19px; color: var(--ink);
  }
  .title {
    position: absolute;
    left: 0; top: 430px; width: 936px; height: 320px;
  }
  .title text {
    font-family: "Sancreek", serif;
    paint-order: stroke fill;
    stroke-linejoin: round;
  }
  .tagline {
    position: absolute;
    left: 0; width: 936px; top: 784px;
    text-align: center;
    font-family: "Bitter", serif; font-weight: 800;
    font-size: 31px; letter-spacing: 2px;
    color: var(--slate);
  }
  .badger-art {
    position: absolute;
    left: 71px; top: 850px; width: 250px; height: 262px;
    background: linear-gradient(120deg, #a09088 0%, #5a463c 100%);
    border-radius: 46% 40% 30% 30%;
  }
  .cup-art {
    position: absolute;
    left: 646px; top: 731px; width: 236px; height: 402px;
    background: linear-gradient(180deg, rgba(90,70,60,0.05) 0%, rgba(90,70,60,0.28) 100%);
    border-radius: 30px;
  }
  .arabica {
    position: absolute;
    left: 349px; top: 935px; width: 256px; height: 34px;
  }
  .arabica span {
    position: absolute; inset: 0;
    display: flex; align-items: center; justify-content: center;
    font-family: "Bitter", serif; font-weight: 800;
    font-size: 17px; color: var(--ink);
  }
  .web {
    position: absolute;
    left: 0; width: 936px; top: 1104px;
    text-align: center;
    font-family: "Bitter", serif; font-weight: 800;
    font-size: 23px; color: var(--ink);
  }
</style>
</head>
<body>
<div class="label">
  <div class="panel"></div>

  <div class="logo-splash" role="img" aria-label="Grunge paint splash with halftone dots and swirls behind the logo"></div>
  <div class="logo-box"></div>
  <div class="logo-plate">
    <div class="logo-name">HERON SIS<br>ROASTERS</div>
  </div>
  <div class="since">Since 2003</div>

  <svg class="title" viewBox="0 0 936 320" aria-label="Heron Sister's Roasters">
    <defs>
      <linearGradient id="rim" x1="0" y1="0" x2="0" y2="1">
        <stop offset="0" stop-color="var(--mocha-dark)"/>
        <stop offset="1" stop-color="var(--mocha-light)"/>
      </linearGradient>
    </defs>
    <text x="476" y="138" text-anchor="middle" font-size="128" textLength="600" lengthAdjust="spacingAndGlyphs"
          fill="var(--ink)" stroke="url(#rim)" stroke-width="18">Heron Sister's</text>
    <text x="476" y="290" text-anchor="middle" font-size="130" textLength="420" lengthAdjust="spacingAndGlyphs"
          fill="var(--ink)" stroke="url(#rim)" stroke-width="18">ROASTERS</text>
  </svg>

  <div class="tagline">LOCALLY ROASTED</div>

  <div class="badger-art" role="img" aria-label="Illustration of a badger sniffing the ground"></div>
  <div class="cup-art" role="img" aria-label="Line drawing of a steaming coffee cup with coffee beans"></div>

  <div class="arabica">
    <svg width="256" height="34" viewBox="0 0 256 34" aria-hidden="true">
      <polygon points="0,0 256,0 250,17 256,34 0,34 6,17" fill="var(--band)"/>
      <rect x="12" y="4" width="232" height="26" fill="#e4e1df"/>
    </svg>
    <span>100% Arabica Coffee</span>
  </div>

  <div class="web">www.heronsisroasters.example</div>
</div>
</body>
</html>
```